New Business Card Design for Engineering and Surveying Company

We need a new design template for our business cards. We are a civil engineering, land surveying and pipeline integrity business. Please see dkhpartners.com for details. We need a bold, new business card design to complement our rebranding and marketing program. We have anew logo and attached vectro file. Please find additional details below. I am available to answer any questions.

Target Market(s)

Contractors, business owners, oil companies

Contact Information for Business Card

Needs to be customizable for different people (name, title, cell)

Font styles to use
Sans Serif
Other font styles liked:
• See eps file

Requirements
Must have
• Example Information:
Trevor Ashcombe

T:409-555-0173
M: 202-555-0148
tashcombe@dkhprtnrs.com

Address: 1875 Pinecrest Parkway, Cedar Hollow, Texas 77590
Email: tolvanrey@dkhpartners.com
Website: www.dkhpartners.com
Nice to have
• I would like the back of the card to have the logo on a bold background with the text below:

[logo]
DORAN KESSLING & PARTNERS
CIVIL ENGINEERING | LAND SURVEYING | PIPELINE INTEGRITY

The reverse side should have the contact information for the person (example above), a smaller version of the logo and a graphic

```html
<!DOCTYPE html>
<html lang="en">
<head>
<meta charset="utf-8">
<title>Doran Kessling &amp; Partners — Business Card</title>
<link rel="stylesheet" href="https://fonts.googleapis.com/css2?family=Montserrat:wght@500;600;700;800&display=swap">
<style>
  :root {
    --stage: #3a3a3a;
    --card: #000000;
    --white: #ffffff;
    --red: #e32434;
    --blue: #2a4aa0;
  }
  * { box-sizing: border-box; margin: 0; padding: 0; }
  html, body { width: 1200px; height: 1200px; overflow: hidden; }
  body {
    background: var(--stage);
    font-family: "Montserrat", sans-serif;
    color: var(--white);
    position: relative;
  }
  .card {
    position: absolute;
    left: 288px;
    width: 624px;
    height: 357px;
    background: var(--card);
  }
  /* Front */
  .card-front { top: 178px; }
  .brand {
    position: absolute;
    top: 150px;
    left: 0;
    right: 0;
    display: flex;
    justify-content: center;
    align-items: center;
    gap: 12px;
  }
  .brand-mark {
    width: 18px;
    height: 18px;
    background: var(--red);
  }
  .brand-name {
    font-weight: 800;
    font-size: 27px;
    letter-spacing: 0.5px;
    color: var(--white);
  }
  .service-band {
    position: absolute;
    top: 287px;
    left: 0;
    right: 0;
    height: 48px;
    background: var(--red);
    border-bottom: 4px solid var(--blue);
    display: flex;
    align-items: center;
    justify-content: center;
    font-weight: 700;
    font-size: 16px;
    letter-spacing: 0.2px;
  }
  /* Back */
  .card-back {
    top: 644px;
    border: 4px solid var(--blue);
  }
  .brand-small {
    position: absolute;
    top: 70px;
    left: 46px;
    display: flex;
    align-items: center;
    gap: 8px;
  }
  .brand-small .brand-mark { width: 10px; height: 10px; }
  .brand-small .brand-name { font-size: 14px; }
  .divider {
    position: absolute;
    top: 126px;
    left: 46px;
    width: 525px;
    height: 3px;
    background: var(--blue);
  }
  .person {
    position: absolute;
    right: 46px;
    top: 100px;
    text-align: right;
  }
  .person-name { font-weight: 700; font-size: 18px; line-height: 22px; }
  .person-title { font-weight: 500; font-size: 17px; margin-top: 10px; }
  .contact {
    position: absolute;
    left: 46px;
    font-weight: 500;
    font-size: 17px;
    line-height: 21px;
  }
  .address { top: 150px; }
  .phones { top: 216px; }
  .phones .label { display: inline-block; width: 36px; }
  .web { top: 280px; }
</style>
</head>
<body>
  <section class="card card-front">
    <div class="brand">
      <span class="brand-mark"></span>
      <span class="brand-name">DORAN KESSLING &amp; PARTNERS</span>
    </div>
    <div class="service-band">CIVIL ENGINEERING | LAND SURVEYING | PIPELINE INTEGRITY</div>
  </section>

  <section class="card card-back">
    <div class="brand-small">
      <span class="brand-mark"></span>
      <span class="brand-name">DORAN KESSLING &amp; PARTNERS</span>
    </div>
    <div class="person">
      <p class="person-name">Trevor Ashcombe</p>
      <p class="person-title">CEO</p>
    </div>
    <div class="divider"></div>
    <p class="contact address">1875 Pinecrest Parkway,<br>Cedar Hollow, Texas 77590</p>
    <p class="contact phones"><span class="label">T :</span>409-555-0173<br><span class="label">M :</span>202-555-0148</p>
    <p class="contact web">tolvanrey@dkhpartners.com<br>www.dkhpartners.com</p>
  </section>
</body>
</html>
```